design an extra page for our profile

we are looking for someone to create another page like the attached but with the below changes:
heading changed to (Construction)
icons changed and names to reflect new services i.e
- Residential Building
- Commercial Building
- Landscaping
- Concrete
- Painting

the very bottom of the page is to stay the same with our office info

```html
<!DOCTYPE html>
<html lang="en">
<head>
<meta charset="utf-8">
<title>Construction Services Flyer</title>
<link href="https://fonts.googleapis.com/css2?family=Montserrat:wght@400;600;700;800&family=Rubik:wght@500&display=swap" rel="stylesheet">
<style>
  :root {
    --brand-blue: #233f96;
    --ink: #1e1e1e;
    --page-bg: #f0f0f0;
    --paper: #ffffff;
    --divider: #d4d6da;
    --photo-light: #f3f5f7;
    --photo-mid: #c9ced4;
    --photo-dark: #8c939b;
  }
  * { margin: 0; padding: 0; box-sizing: border-box; }
  html, body { width: 783px; height: 1200px; overflow: hidden; background: var(--page-bg); }
  .flyer {
    position: absolute; left: 0; top: 47px; width: 783px; height: 1106px;
    background: var(--paper); overflow: hidden;
    box-shadow: 0 2px 10px rgba(0,0,0,0.18);
    font-family: 'Montserrat', sans-serif;
  }
  .header {
    position: absolute; left: 0; top: 0; width: 100%; height: 207px;
    background: var(--brand-blue); color: #fff; text-align: center;
  }
  .header__title {
    position: absolute; top: 55px; width: 100%;
    font-size: 38px; line-height: 44px; font-weight: 800; letter-spacing: 1px;
  }
  .header__intro {
    position: absolute; top: 112px; width: 100%;
    font-size: 18px; line-height: 22px; font-weight: 400; letter-spacing: 0.3px;
  }
  .office-photo {
    position: absolute; left: 0; top: 300px; width: 100%; height: 667px;
    background: linear-gradient(180deg, var(--paper) 0%, var(--photo-light) 25%, var(--photo-mid) 55%, var(--photo-dark) 78%, var(--photo-mid) 100%);
  }
  .service {
    position: absolute; width: 170px; margin-left: -85px; text-align: center;
  }
  .service__icon { display: block; margin: 0 auto; }
  .service__label {
    margin-top: 8px;
    font-family: 'Rubik', sans-serif; font-weight: 500;
    font-size: 22px; line-height: 26px; color: var(--ink); letter-spacing: 0.3px;
  }
  .divider { position: absolute; width: 2px; background: linear-gradient(180deg, rgba(212,214,218,0), var(--divider) 30%, var(--divider) 70%, rgba(212,214,218,0)); }
  .footer {
    position: absolute; left: 0; top: 976px; width: 100%; height: 130px;
    background: var(--brand-blue); color: #fff;
  }
  .footer__brand {
    position: absolute; left: 47px; top: 44px; width: 135px; text-align: center;
    font-size: 28px; line-height: 32px; font-weight: 600; letter-spacing: 1px;
  }
  .footer__line {
    position: absolute; font-size: 12px; font-weight: 700; letter-spacing: 0.2px;
    display: flex; align-items: center; gap: 5px; white-space: nowrap;
  }
  .footer__sep { position: absolute; width: 1px; height: 14px; border-left: 1px dashed rgba(255,255,255,0.6); }
</style>
</head>
<body>
<main class="flyer">
  <header class="header">
    <h1 class="header__title">CONSTRUCTION</h1>
    <p class="header__intro">As New Tenants To The Building And As A Way Of Introducing<br>Ourselves We Would Like To Offer A 10% Discount On Any<br>Of The Below Services.</p>
  </header>

  <div class="office-photo" role="img" aria-label="Bright open-plan office with white desks, black chairs and city-view windows"></div>

  <svg width="0" height="0" style="position:absolute">
    <defs>
      <g id="badge">
        <circle cx="42" cy="42" r="40" fill="none" stroke="#233f96" stroke-width="1.2" stroke-dasharray="1.5 2.5"/>
        <circle cx="42" cy="42" r="36" fill="#233f96"/>
        <circle cx="42" cy="42" r="29" fill="#fff"/>
      </g>
    </defs>
  </svg>

  <div class="divider" style="left:292px; top:252px; height:148px;"></div>
  <div class="divider" style="left:489px; top:252px; height:148px;"></div>
  <div class="divider" style="left:389px; top:420px; height:152px;"></div>

  <div class="service" style="left:193px; top:250px;">
    <svg class="service__icon" width="84" height="84" viewBox="0 0 84 84"><use href="#badge"/>
      <g fill="none" stroke="#1e1e1e" stroke-width="1.6"><rect x="31" y="34" width="14" height="20"/><rect x="45" y="40" width="9" height="14"/><path d="M34 39h3M39 39h3M34 44h3M39 44h3M34 49h3M39 49h3M48 45h3M48 49h3M28 54h28"/></g>
    </svg>
    <div class="service__label">Residential<br>Building</div>
  </div>

  <div class="service" style="left:392px; top:250px;">
    <svg class="service__icon" width="84" height="84" viewBox="0 0 84 84"><use href="#badge"/>
      <g fill="none" stroke="#1e1e1e" stroke-width="1.6"><rect x="32" y="29" width="20" height="26"/><rect x="35" y="33" width="5" height="5"/><rect x="44" y="33" width="5" height="5"/><rect x="35" y="41" width="5" height="5"/><rect x="44" y="41" width="5" height="5"/><path d="M39 55v-5h6v5M29 55h26"/></g>
    </svg>
    <div class="service__label">Commercial<br>Building</div>
  </div>

  <div class="service" style="left:582px; top:250px;">
    <svg class="service__icon" width="84" height="84" viewBox="0 0 84 84"><use href="#badge"/>
      <g fill="none" stroke="#1e1e1e" stroke-width="1.6"><circle cx="38" cy="36" r="6"/><path d="M38 42v11M46 38c4 0 7 3 7 7h-14c0-4 3-7 7-7zM46 45v8M29 54h26M32 54l2-4M50 54l2-4"/></g>
    </svg>
    <div class="service__label">Landscaping</div>
  </div>

  <div class="service" style="left:288px; top:433px;">
    <svg class="service__icon" width="84" height="84" viewBox="0 0 84 84"><use href="#badge"/>
      <g fill="none" stroke="#1e1e1e" stroke-width="1.6"><path d="M28 48v-9h8l4 5h6v4zM46 44l3-9 7 3-3 8z"/><circle cx="33" cy="50" r="3"/><circle cx="47" cy="50" r="3"/></g>
    </svg>
    <div class="service__label">Concrete</div>
  </div>

  <div class="service" style="left:495px; top:433px;">
    <svg class="service__icon" width="84" height="84" viewBox="0 0 84 84"><use href="#badge"/>
      <g fill="none" stroke="#1e1e1e" stroke-width="1.6"><path d="M31 40h14v14H31zM38 44c-2 3-2 5 0 6 2-1 2-3 0-6zM45 38l8-8 3 3-8 8"/></g>
    </svg>
    <div class="service__label">Painting</div>
  </div>

  <footer class="footer">
    <div class="footer__brand">KESTON</div>
    <div class="footer__line" style="left:200px; top:42px;">
      <svg width="10" height="10" viewBox="0 0 10 10"><path d="M2 1l2 0 1 2-1.2 1a6 6 0 002.2 2.2L7 5l2 1v2c0 .6-.4 1-1 1A8 8 0 011 2c0-.6.4-1 1-1z" fill="#fff"/></svg>
      HOME OFFICE: 1300482915
    </div>
    <div class="footer__sep" style="left:446px; top:43px;"></div>
    <div class="footer__line" style="left:458px; top:42px;">
      <svg width="9" height="11" viewBox="0 0 9 11"><path d="M4.5 10.5S1 6.5 1 4.2a3.5 3.5 0 017 0c0 2.3-3.5 6.3-3.5 6.3z" fill="none" stroke="#fff" stroke-width="1.4"/><circle cx="4.5" cy="4.2" r="1.2" fill="#fff"/></svg>
      Suite 2.04, 18 Harbour Lane Northvale
    </div>
    <div class="footer__line" style="left:200px; top:70px;">
      <svg width="10" height="10" viewBox="0 0 10 10"><g fill="none" stroke="#fff" stroke-width="1"><circle cx="5" cy="5" r="4"/><ellipse cx="5" cy="5" rx="1.8" ry="4"/><path d="M1 5h8"/></g></svg>
      WWW.KESTON-SERVICES.COM.AU
    </div>
    <div class="footer__sep" style="left:446px; top:71px;"></div>
    <div class="footer__line" style="left:458px; top:70px;">Sydney | Canberra | Brisbane | Melbourne</div>
  </footer>
</main>
</body>
</html>
```